Workers comp/Business Ins/ Payroll- Postcard

I own an insurance agency.  I'm interested in getting some professional advice on how to design a message for what i want to sell.  The products I want to sell are 1) Workers compensation 2) business Insurance 3) Payroll processing. They are integrated together but I'm not sure if it's too much to put on a postcard and if I don't put it on a postcard I could be missing out on sales.
I have the ability to look up what Insurance company a business has their workers compensation  policy with, along with their expiration date.  Based on that information I can tell if the business is overpaying for their Workers compensation. insurance. Most companies are overpaying so I can usually save a company money very quickly if I can get in front of them. Some businesses work with a broker such as myself and buy a policy. When it's done this way, the business ESTIMATES his payroll for the year and at the end of the year they have to complete an audit to find out the actual payroll. Based on audit, they will either owe more money if they were low or get money back if they were high. The other way a business buys a workers comp. policy is with their payroll company. The payroll company will place the policy on Pay -as- you -go which means when you pay your employees every week they  will also calculate how much the workers comp premium is for the week and take that amount out of their checking account. This method avoids large down payments, helps with cash flow and should be very accurate at the end of the policy term.  This is by far the best way to do this for the businessowner. My company also has payroll company and we do this for the insured as well. However, most payroll company's such as QVR and Wagemint charge the customer $15 every time they do this so if it's weekly it is another $780 a year.  We also complete the insured's audit for them which is a big headache for the businessowner.
One of our biggest benefits of doing business with our company is we have a  Rate Anchor Forever. When you sign up your base price will never increase. Payroll companies are famous for "discounting a new client" only to increase the rate in a few months later. Our service is also superior to the other payroll companies who use overseas service centers. We have staff within our office and we can answer questions quickly. We usually save businesses money on  their Payroll processing but it's not what we focus on- We focus on the Service.
Business Insurance- One of our main companies that we represent is Tolvan Insurance. Tolvan is very competitive and we usually write business accounts where we save the business owner money but offer superior coverages.
in summary, I'm offering 1) better workers compensation rates 2) Pay as you go workers comp. 3) Rate Anchor, audits done for you, and superior customer service with our payroll company 4) savings on their business insurance with superior coverages.
Sometimes when we talk to an insured we may start with just their payroll and later get the WC and business liability. Each account is different and we do not pressure people to make decisions and we do what is right for them.  The biggest takeaway is we take some things off the plate for the businessowner where they can make just one phone call to get what they need done.  Our Website is www.brackwell-partners.net. my email is tomr@brackwell-partners.net if you have any questions.
Thank You
Tom Rusk

Target Market(s)
Small business owners 1-50 employees
Industry/Entity Type
Insurance and Payroll
Font styles to use
Other font styles liked:
- Let designer choose

Colors
Designer to choose colors to be used in the design.
Requirements
Must have
- It shouldn't be boring- needs to stand out- can use 6x11 inch postcard

Nice to have
- I like humor but not a must

Should not have
- Nothing I can think of

```html
<!DOCTYPE html>
<html lang="en">
<head>
<meta charset="utf-8">
<title>Brackwell Partners Insurance – Postcard</title>
<link href="https://fonts.googleapis.com/css2?family=Montserrat:wght@400;500;600;700;800&display=swap" rel="stylesheet">
<style>
  :root{
    --maroon:#7d3035;
    --maroon-deep:#6a2329;
    --maroon-shade:#5c1e23;
    --ink:#1b1b1b;
    --grey:#7a7a7a;
    --backdrop:#cfcfcf;
    --paper:#ffffff;
  }
  *{margin:0;padding:0;box-sizing:border-box}
  html,body{width:914px;height:1200px;overflow:hidden;background:var(--backdrop)}
  body{font-family:'Montserrat',sans-serif;position:relative;color:var(--ink)}
  .card{position:absolute;left:91px;width:733px;height:463px;background:var(--paper);overflow:hidden;box-shadow:0 14px 14px -6px rgba(0,0,0,.28)}
  .card--front{top:86px}
  .card--back{top:618px}
  .abs{position:absolute}
  .shapes{position:absolute;left:0;top:0}
  .photo{position:absolute;left:0;top:0;width:733px;height:384px;
    clip-path:polygon(445px 0,733px 0,733px 384px,347px 384px);
    background:linear-gradient(125deg,#b9cf98 0%,#dcc2a9 38%,#c9a58c 55%,#a99886 75%,#6f9248 100%)}
  .brand{display:flex;align-items:center;gap:8px;font-weight:700;color:var(--maroon);letter-spacing:.5px}
  .brand__mark{width:14px;height:14px;background:var(--grey)}
  .front-brand{left:58px;top:50px;font-size:21px}
  .headline{left:35px;font-weight:700;color:#fff;font-size:38px;line-height:1;letter-spacing:.5px}
  .headline--muted{color:var(--maroon-shade)}
  .subline{left:35px;top:243px;font-size:14px;font-weight:500;color:#fff}
  .services{left:35px;top:284px;list-style:none;color:#fff;font-weight:700;font-size:14px;letter-spacing:.2px}
  .services li{display:flex;align-items:center;gap:6px;height:21.5px}
  .services li::before{content:"";width:9px;height:9px;background:#fff}
  .cta-label{left:35px;top:370px;font-size:13px;font-weight:700}
  .cta-phone{left:35px;top:384px;font-size:31px;font-weight:700;color:var(--maroon);letter-spacing:-.3px}
  .cta-web{left:35px;top:419px;font-size:13px;font-weight:700}
  .front-address{right:53px;top:396px;text-align:right;font-size:12.5px;font-weight:700;line-height:18px}
  .back-photo{position:absolute;left:0;top:0;width:733px;height:463px;
    clip-path:polygon(0 0,340px 0,449px 463px,0 463px);
    background:linear-gradient(160deg,#8a3a3e 0%,var(--maroon) 45%,#6e272c 100%)}
  .back-title{left:35px;top:33px;color:#fff;font-size:27px;line-height:29px;font-weight:500;letter-spacing:.3px}
  .back-title strong{font-weight:800}
  .mission{left:35px;top:119px;color:#fff;font-size:11px;line-height:14px;width:320px}
  .rule{left:35px;width:209px;height:2px;background:#fff}
  .offer-title{left:35px;top:245px;color:#fff;font-size:22px;font-weight:800;letter-spacing:.3px}
  .offers{left:35px;top:276px;list-style:none;color:#fff;font-size:12.3px;line-height:14px;width:360px}
  .offers li{display:flex;gap:5px;margin-bottom:7.5px}
  .offers svg{flex:none;margin-top:1px}
  .back-cta{left:35px;top:407px;color:#fff;font-size:21px;font-weight:800;letter-spacing:.2px}
  .stamp{left:609px;top:34px;width:84px;height:83px;border:1.5px solid var(--grey)}
  .address-line{left:533px;width:160px;height:1.5px;background:var(--grey)}
  .back-address{right:40px;top:239px;text-align:right;color:var(--grey);font-size:12px;font-weight:700;line-height:14px}
  .back-brand{right:40px;top:392px;font-size:16px}
</style>
</head>
<body>

<section class="card card--front">
  <div class="photo" role="img" aria-label="Photo of a smiling family outdoors: father carrying his daughter piggyback beside the mother"></div>
  <svg class="shapes" width="733" height="463" aria-hidden="true">
    <polygon points="0,123 420,123 347,384 325,384 332,361 0,361" fill="var(--maroon)"/>
    <polygon points="0,273 372,273 347,361 0,361" fill="var(--maroon-deep)"/>
  </svg>

  <div class="abs brand front-brand"><span class="brand__mark"></span>BRACKWELL PARTNERS</div>

  <div class="abs headline" style="top:139px">INSURING</div>
  <div class="abs headline headline--muted" style="top:174px">YOUR NEEDS</div>
  <div class="abs headline" style="top:209px">TODAY!</div>
  <div class="abs subline">Savings On Their Business Insurance</div>

  <ul class="abs services">
    <li>WORKERS COMPENSATION</li>
    <li>BUSINESS INSURANCE</li>
    <li>PAYROLL PROCESSING</li>
  </ul>

  <div class="abs cta-label">CALL US NOW!</div>
  <div class="abs cta-phone">585-555-0142</div>
  <div class="abs cta-web">www.brackwell-partners.net</div>

  <div class="abs front-address">220 LINDEN RIDGE ROAD | HARLOW, NY 14501<br>TOLL-FREE: 844.555.0199 | FAX: 585.555.0143</div>
</section>

<section class="card card--back">
  <div class="back-photo" role="img" aria-label="Faint maroon-toned photo of a business owner at work"></div>

  <h2 class="abs back-title">SUITABLE<br><strong>POLICIES</strong> FOR<br>YOUR NEEDS</h2>
  <p class="abs mission">Our mission is to be your most Trusted Advisor for all of<br>your insurance needs, from home and auto plans, to life<br>insurance, to the specialty protections required for your<br>business. We are consultative and develop an insurance<br>program specific to your needs, providing just the right<br>amount of protection suitable for your assets, goals and<br>situation.</p>

  <div class="abs rule" style="top:229px"></div>
  <h3 class="abs offer-title">I'M OFFERING</h3>
  <ul class="abs offers">
    <li><svg width="12" height="12" viewBox="0 0 12 12"><circle cx="6" cy="6" r="6" fill="#fff"/><path d="M3.2 6.2l2 2 3.8-4" stroke="var(--maroon)" stroke-width="1.6" fill="none"/></svg>Better Workers Compensation Rates</li>
    <li><svg width="12" height="12" viewBox="0 0 12 12"><circle cx="6" cy="6" r="6" fill="#fff"/><path d="M3.2 6.2l2 2 3.8-4" stroke="var(--maroon)" stroke-width="1.6" fill="none"/></svg>Pay As You Go Workers Comp.</li>
    <li><svg width="12" height="12" viewBox="0 0 12 12"><circle cx="6" cy="6" r="6" fill="#fff"/><path d="M3.2 6.2l2 2 3.8-4" stroke="var(--maroon)" stroke-width="1.6" fill="none"/></svg><span>Rate Anchor, Audits Done For You, And Superior<br>Customer Service With Our Payroll Company</span></li>
    <li><svg width="12" height="12" viewBox="0 0 12 12"><circle cx="6" cy="6" r="6" fill="#fff"/><path d="M3.2 6.2l2 2 3.8-4" stroke="var(--maroon)" stroke-width="1.6" fill="none"/></svg><span>Savings On Their Business Insurance With Superior<br>Coverages.</span></li>
  </ul>
  <div class="abs rule" style="top:394px"></div>
  <div class="abs back-cta">CALL US NOW! 585-555-0142</div>

  <div class="abs stamp"></div>
  <div class="abs address-line" style="top:147px"></div>
  <div class="abs address-line" style="top:173px"></div>
  <div class="abs address-line" style="top:199px"></div>

  <div class="abs back-address">220 LINDEN RIDGE ROAD<br>HARLOW, NY 14501</div>
  <div class="abs brand back-brand"><span class="brand__mark"></span>BRACKWELL PARTNERS</div>
</section>

</body>
</html>
```